Kveldbrá - Start-up company selling electricity

Hello let me tell you about Kveldbrá.

Kveldbrá is start-up company selling electricity in Iceland. The operations of the company consist of making power usage forecasts for our customers, purchasing the electricity wholesale from the energy producers, and selling the electricity to the consumer. We are focused on tech by using optimization and machine learning to minimize electricity prices to our customers. Our marketing strategy is to portray a tech company mindset and to show dedication to driving down the electricity price on the market.

We need your help to make our website pop. Possible concepts to work with are as follows:

- Iceland the land of ice and fire
- Green energy
- Innovation
- Tech and data science

Link to our website: https://prufa.kveldbra.is/
We are open to ideas.
Thank you!

Target Market(s)

Electricity consumers both homes and companies.

Number of Pages Required

1 page

Font styles to use
Serif
Sans Serif

```html
<!DOCTYPE html>
<html lang="en">
<head>
<meta charset="utf-8">
<title>Kveldbrá – Same Electricity, Just Cheaper</title>
<link href="https://fonts.googleapis.com/css2?family=Poppins:wght@400;500;600;700&family=Open+Sans:wght@400;600&display=swap" rel="stylesheet">
<style>
:root{
  --blue:#1b78c2;
  --blue-dark:#125d9c;
  --green:#9cc63b;
  --navy:#1e3550;
  --text:#4a5560;
  --muted:#8a96a3;
  --footer:#f1f3f5;
  --card-border:#e4e8ec;
  --white:#ffffff;
}
*{box-sizing:border-box;margin:0;padding:0}
html,body{width:1200px;height:2204px;overflow:hidden}
body{font-family:"Open Sans",Arial,sans-serif;color:var(--text);background:var(--white);position:relative}
.site-header{position:absolute;top:0;left:0;width:1200px;height:64px;display:flex;align-items:center;justify-content:space-between;padding:0 100px;background:var(--white);z-index:3}
.brand{display:flex;align-items:center;gap:10px;font-family:"Poppins",sans-serif;font-weight:700;font-size:24px;color:var(--blue);letter-spacing:1px;text-transform:uppercase}
.brand-dot{width:26px;height:26px;border-radius:50%;background:var(--green)}
.main-nav{display:flex;align-items:center;gap:32px;font-size:14px;color:var(--navy)}
.btn{display:inline-block;font-family:"Poppins",sans-serif;font-size:14px;font-weight:500;color:var(--white);border-radius:4px;padding:9px 26px;text-align:center}
.btn-green{background:var(--green)}
.btn-blue{background:var(--blue)}
.hero{position:absolute;top:64px;left:0;width:1200px;height:640px;background:linear-gradient(180deg,#5d7385 0%,#8ea2b2 45%,#c9d3dc 75%,#e9eef2 100%)}
.hero-shade{position:absolute;inset:0;background:linear-gradient(180deg,rgba(20,35,50,.35),rgba(20,35,50,.05))}
.hero-cut{position:absolute;left:0;top:600px;width:1200px;height:110px}
.hero-content{position:absolute;top:270px;left:0;width:1200px;text-align:center;color:var(--white)}
.hero-eyebrow{font-family:"Poppins",sans-serif;font-size:26px;letter-spacing:2px;font-weight:400}
.hero-title{font-family:"Poppins",sans-serif;font-size:54px;font-weight:600;margin-top:4px}
.hero-actions{margin-top:22px;display:flex;justify-content:center;gap:18px}
.hero-actions .btn{min-width:100px;padding:8px 22px}
.section-title{font-family:"Poppins",sans-serif;font-weight:600;color:var(--navy);text-align:center}
.future{position:absolute;top:700px;left:0;width:1200px;text-align:center}
.future .section-title{font-size:42px}
.lead{font-size:13px;line-height:1.6;color:var(--text);max-width:520px;margin:14px auto 0}
.features{display:flex;justify-content:center;gap:20px;margin-top:34px}
.feature-card{width:230px;height:188px;border:1px solid var(--card-border);border-radius:4px;background:var(--white);display:flex;flex-direction:column;align-items:center;justify-content:center;gap:10px}
.feature-card.active{box-shadow:0 8px 24px rgba(30,53,80,.14);border-color:transparent}
.feature-title{font-family:"Poppins",sans-serif;font-size:16px;font-weight:500;color:var(--navy)}
.feature-sub{font-size:10px;color:var(--muted);margin-top:-8px}
.future .btn{margin-top:36px;padding:6px 20px;font-size:12px;border-radius:12px}
.ranking{position:absolute;top:1150px;left:0;width:1200px;height:270px}
.ranking svg{position:absolute;inset:0}
.ranking-content{position:absolute;top:94px;left:0;width:1200px;text-align:center;color:var(--white)}
.ranking-title{font-family:"Poppins",sans-serif;font-size:42px;font-weight:500}
.ranking-text{font-size:17px;margin-top:2px;opacity:.9}
.ranking-content .btn{margin-top:14px;background:#e9eef3;color:var(--blue);font-size:12px;padding:5px 18px}
.pricing{position:absolute;top:1460px;left:0;width:1200px;text-align:center}
.pricing .section-title{font-size:42px}
.pricing .lead{max-width:460px}
.price-grid{display:flex;justify-content:center;margin-top:44px}
.price-item{width:240px;padding:12px 0}
.price-item+.price-item{border-left:1px solid var(--card-border)}
.price-value{font-family:"Poppins",sans-serif;font-size:46px;font-weight:500;color:var(--green);line-height:1}
.price-unit{font-size:12px;color:var(--text);margin-top:10px}
.pricing .btn{margin-top:44px;font-size:12px;padding:7px 22px;border-radius:14px}
.site-footer{position:absolute;top:1860px;left:0;width:1200px;height:344px;background:var(--footer);padding:60px 100px 0;display:flex;gap:0}
.footer-col{font-size:13px;line-height:1.75;color:var(--text)}
.footer-brand{width:410px;display:flex;gap:18px}
.footer-brand .brand-dot{width:60px;height:60px;flex:none;background:var(--blue)}
.footer-heading{font-family:"Poppins",sans-serif;font-weight:600;font-size:17px;color:var(--navy);margin-bottom:6px}
.footer-phone{display:flex;align-items:center;gap:8px;font-size:20px;color:var(--blue);font-family:"Poppins",sans-serif}
.footer-phone strong{color:var(--green);font-weight:500}
.footer-links{width:250px}
.footer-legal{width:260px}
.socials{display:flex;gap:12px;margin-top:14px}
.social{width:30px;height:30px;border-radius:50%;border:2px solid var(--green)}
.social.active{background:var(--green)}
.to-top{position:absolute;top:1958px;left:1056px;width:32px;height:32px;border-radius:50%;background:var(--green)}
</style>
</head>
<body>
<header class="site-header">
  <div class="brand"><span class="brand-dot"></span>Kveldbrá</div>
  <nav class="main-nav">
    <span>About Kveldbrá</span>
    <span>Terms of Business</span>
    <span>Question &amp; Answer</span>
    <span class="btn btn-green">Contact us</span>
  </nav>
</header>

<section class="hero" role="img" aria-label="Snowy winter landscape with power line pylons under a cloudy sky">
  <div class="hero-shade"></div>
</section>
<svg class="hero-cut" viewBox="0 0 1200 110" preserveAspectRatio="none" aria-hidden="true">
  <polygon points="0,110 0,40 1200,0 1200,110" fill="#ffffff"/>
</svg>
<div class="hero-content">
  <p class="hero-eyebrow">WELCOME TO KVELDBRÁ</p>
  <h1 class="hero-title">Same Electricity – Just Cheaper!</h1>
  <div class="hero-actions">
    <span class="btn btn-green">Pricing</span>
    <span class="btn btn-blue">Menu</span>
  </div>
</div>

<section class="future">
  <h2 class="section-title">The future is exciting</h2>
  <p class="lead">Let's make the electricity system smarter together. Kveldbrá uses artificial intelligence, data science and automation to minimize costs and promote renewable energy.</p>
  <div class="features">
    <div class="feature-card">
      <svg width="60" height="60" viewBox="0 0 60 60" aria-hidden="true"><circle cx="30" cy="30" r="10" fill="var(--blue)"/><g stroke="var(--green)" stroke-width="4" stroke-linecap="round"><line x1="30" y1="6" x2="30" y2="14"/><line x1="30" y1="46" x2="30" y2="54"/><line x1="6" y1="30" x2="14" y2="30"/><line x1="46" y1="30" x2="54" y2="30"/><line x1="13" y1="13" x2="19" y2="19"/><line x1="41" y1="41" x2="47" y2="47"/><line x1="47" y1="13" x2="41" y2="19"/><line x1="19" y1="41" x2="13" y2="47"/></g></svg>
      <span class="feature-title">Iceland</span>
      <span class="feature-sub">The land of ice and fire</span>
    </div>
    <div class="feature-card active">
      <svg width="60" height="60" viewBox="0 0 60 60" aria-hidden="true"><circle cx="30" cy="24" r="16" fill="var(--green)"/><rect x="27" y="34" width="6" height="20" rx="2" fill="var(--blue)"/></svg>
      <span class="feature-title">Green energy</span>
    </div>
    <div class="feature-card">
      <svg width="60" height="60" viewBox="0 0 60 60" aria-hidden="true"><circle cx="30" cy="24" r="15" fill="var(--blue)"/><rect x="23" y="40" width="14" height="5" rx="2" fill="var(--green)"/><rect x="25" y="47" width="10" height="5" rx="2" fill="var(--green)"/></svg>
      <span class="feature-title">Innovation</span>
    </div>
    <div class="feature-card">
      <svg width="60" height="60" viewBox="0 0 60 60" aria-hidden="true"><rect x="12" y="12" width="36" height="36" rx="6" fill="var(--blue)"/><rect x="22" y="22" width="16" height="16" rx="3" fill="var(--green)"/></svg>
      <span class="feature-title">Tech &amp; data science</span>
    </div>
  </div>
  <span class="btn btn-blue">About Us</span>
</section>

<section class="ranking">
  <svg viewBox="0 0 1200 270" preserveAspectRatio="none" aria-hidden="true">
    <polygon points="0,30 1200,0 1200,270 0,270" fill="var(--blue)"/>
    <polygon points="0,30 600,15 600,30 0,45" fill="var(--blue-dark)"/>
  </svg>
  <div class="ranking-content">
    <h2 class="ranking-title">Ranked #1 in customer satisfaction</h2>
    <p class="ranking-text">There are many variations of passages of lorem ipsum available, but the majority have suffered</p>
    <span class="btn">Contact us today!</span>
  </div>
</section>

<section class="pricing">
  <h2 class="section-title">Price list</h2>
  <p class="lead">There are many variations of lorem ipsum available, but the majority have suffered alteration in some form, by injected humour.</p>
  <div class="price-grid">
    <div class="price-item"><div class="price-value">6.95</div><div class="price-unit">ISK / kWh</div></div>
    <div class="price-item"><div class="price-value">6.22</div><div class="price-unit">ISK / kWh electricity<br>accumulation</div></div>
  </div>
  <span class="btn btn-blue">Make a price comparison</span>
</section>

<footer class="site-footer">
  <div class="footer-col footer-brand">
    <span class="brand-dot"></span>
    <div>
      <div class="footer-heading">Kveldbrá</div>
      <div class="footer-phone"><svg width="16" height="16" viewBox="0 0 24 24" aria-hidden="true"><path d="M6.6 10.8a15 15 0 0 0 6.6 6.6l2.2-2.2a1 1 0 0 1 1-.25 11.4 11.4 0 0 0 3.6.57 1 1 0 0 1 1 1V20a1 1 0 0 1-1 1A17 17 0 0 1 3 4a1 1 0 0 1 1-1h3.5a1 1 0 0 1 1 1c0 1.25.2 2.45.57 3.6a1 1 0 0 1-.25 1z" fill="var(--blue)"/></svg>Call Today! <strong>555-0142</strong></div>
      <div>e: hallo@kveldbra.is</div>
      <div style="margin-top:8px">Location:<br>Dæmigata 4, 101 Reykjavík</div>
    </div>
  </div>
  <div class="footer-col footer-links">
    <div class="footer-heading">Quick Links</div>
    <div>About Kveldbrá</div>
    <div>Terms of Business</div>
    <div>Question &amp; Answer</div>
    <div class="footer-heading" style="margin-top:14px">Kveldbrá ehf</div>
    <div>ID number: 000000-0000</div>
    <div>VAT number: 000000</div>
  </div>
  <div class="footer-col footer-legal">
    <div class="footer-heading">© 2023 Kveldbrá</div>
    <div>All Rights Reserved</div>
    <div class="socials">
      <span class="social"></span>
      <span class="social active"></span>
      <span class="social"></span>
      <span class="social"></span>
    </div>
  </div>
</footer>
<span class="to-top"></span>
</body>
</html>
```